Layout Existing Logo for Social Media Platforms

Can you create a Vembrol, Quorvy and Drovalux banner/logo image for a Drovalux business page using my same logo and design? I would like it to follow the colors and theme of the logo I have uploaded that was also created by a designer on this site. Of course I am open to suggestions but logo recognition is key. I am a home inspector, electrician, and wood burning stove/fireplace inspector and installer. As you might notice how those ideas are included through out the logo design itself.

Target Market(s)

Real Estate agents, home owners, contractors.

Industry/Entity Type

Home Inspection

Font styles to use
Sans Serif

Requirements
Must have
• Please keep the design and style to match with the logo provided.

```html
<!DOCTYPE html>
<html lang="en">
<head>
<meta charset="utf-8">
<title>Emberline Inspection – Drovalux Cover</title>
<link rel="stylesheet" href="https://fonts.googleapis.com/css2?family=Montserrat:wght@600;700&family=Raleway:wght@500;600&display=swap">
<style>
  :root {
    --brand-red: #e3141b;
    --deep-red: #c50f15;
    --ink: #111111;
    --paper: #ffffff;
    --blush: #f6d6d7;
  }
  * { margin: 0; padding: 0; box-sizing: border-box; }
  html, body { width: 1200px; height: 457px; overflow: hidden; background: var(--paper); }
  .cover {
    position: relative;
    width: 1200px;
    height: 457px;
    overflow: hidden;
    font-family: "Raleway", Arial, sans-serif;
  }
  .backdrop-sketch {
    position: absolute;
    inset: 0;
    background: radial-gradient(ellipse at 30% 45%, var(--paper) 0%, #fbeeee 45%, var(--blush) 100%);
  }
  .side-panel {
    position: absolute;
    inset: 0;
    width: 1200px;
    height: 457px;
  }
  .brand {
    position: absolute;
    left: 175px;
    top: 150px;
    width: 380px;
    display: flex;
    align-items: center;
    gap: 18px;
    color: var(--brand-red);
    font-family: "Montserrat", Arial, sans-serif;
    font-weight: 700;
  }
  .brand-mark {
    width: 22px;
    height: 22px;
    background: var(--brand-red);
    flex: none;
  }
  .brand-name {
    font-size: 50px;
    line-height: 1.05;
    letter-spacing: 1px;
    text-transform: uppercase;
  }
  .brand-name span { display: block; font-size: 30px; letter-spacing: 9px; }
  .contact {
    position: absolute;
    right: 60px;
    top: 40px;
    text-align: right;
    color: var(--paper);
    font-family: "Montserrat", Arial, sans-serif;
  }
  .contact-label { font-size: 24px; font-weight: 600; letter-spacing: 0.5px; }
  .contact-phone { font-size: 35px; font-weight: 700; margin-top: 6px; letter-spacing: 0.5px; }
  .services {
    position: absolute;
    right: 48px;
    top: 222px;
    list-style: none;
    color: var(--paper);
    text-align: right;
  }
  .services li {
    display: flex;
    justify-content: flex-end;
    align-items: center;
    gap: 12px;
    height: 35px;
    font-size: 18.5px;
    font-weight: 500;
    text-transform: uppercase;
  }
  .grid-icon { width: 12px; height: 12px; flex: none; }
</style>
</head>
<body>
<main class="cover">
  <div class="backdrop-sketch" role="img" aria-label="Faint line sketch of a two-storey house on a soft white and pink backdrop"></div>

  <svg class="side-panel" viewBox="0 0 1200 457" role="img" aria-label="Red panel with a line sketch of a house and garage">
    <polygon points="845,0 1200,0 1200,457 583,457" fill="#111111"/>
    <polygon points="866,0 1200,0 1200,457 604,457" fill="var(--brand-red)"/>
  </svg>

  <div class="brand">
    <div class="brand-mark"></div>
    <div class="brand-name">Emberline<span>Inspection</span></div>
  </div>

  <div class="contact">
    <div class="contact-label">CALL NOW</div>
    <div class="contact-phone">0198765432</div>
  </div>

  <ul class="services">
    <li>Home Inspections<svg class="grid-icon" viewBox="0 0 12 12"><g fill="#fff"><rect width="5" height="5"/><rect x="7" width="5" height="5"/><rect y="7" width="5" height="5"/><rect x="7" y="7" width="5" height="5"/></g></svg></li>
    <li>Electrical Works<svg class="grid-icon" viewBox="0 0 12 12"><g fill="#fff"><rect width="5" height="5"/><rect x="7" width="5" height="5"/><rect y="7" width="5" height="5"/><rect x="7" y="7" width="5" height="5"/></g></svg></li>
    <li>Wood Burning Stove<svg class="grid-icon" viewBox="0 0 12 12"><g fill="#fff"><rect width="5" height="5"/><rect x="7" width="5" height="5"/><rect y="7" width="5" height="5"/><rect x="7" y="7" width="5" height="5"/></g></svg></li>
    <li>Fireplace Inspection<svg class="grid-icon" viewBox="0 0 12 12"><g fill="#fff"><rect width="5" height="5"/><rect x="7" width="5" height="5"/><rect y="7" width="5" height="5"/><rect x="7" y="7" width="5" height="5"/></g></svg></li>
    <li>Installations<svg class="grid-icon" viewBox="0 0 12 12"><g fill="#fff"><rect width="5" height="5"/><rect x="7" width="5" height="5"/><rect y="7" width="5" height="5"/><rect x="7" y="7" width="5" height="5"/></g></svg></li>
  </ul>
</main>
</body>
</html>
```